Larkfield milling Business Card Design

Rice milling

Industry/Entity Type

Business

Contact Information for Business Card

DALE VOSKO
Construction Manager
LARKFIELD MILLING CO., LLC
3870 WILBUR HASTINGS DRIVE
PINE BLUFF, AR 71601
CELL: 501-555-0142
dalevosko@larkfieldmills.example

```html
<!DOCTYPE html>
<html lang="en">
<head>
<meta charset="utf-8">
<title>Larkfield Milling – Business Card</title>
<link rel="stylesheet" href="https://fonts.googleapis.com/css2?family=PT+Sans:wght@400;700&display=swap">
<style>
  :root {
    --backdrop: #808080;
    --gold: #fdd000;
    --gold-deep: #e9b800;
    --teal: #11968c;
    --teal-band: #17a89c;
    --ink: #050505;
    --paper: #ffffff;
    --grain-light: #f4cf6a;
    --grain-dark: #d99a2b;
  }
  html, body {
    margin: 0;
    width: 1200px;
    height: 1000px;
    overflow: hidden;
    background: var(--backdrop);
    font-family: "PT Sans", "Myriad Pro", sans-serif;
  }
  .card {
    position: absolute;
    left: 58px;
    top: 270px;
    width: 1085px;
    height: 635px;
    overflow: hidden;
    background: var(--ink);
  }
  .card-bands {
    position: absolute;
    inset: 0;
  }
  .grain-photo {
    position: absolute;
    border-radius: 50%;
    background: radial-gradient(ellipse at center, var(--grain-light) 0%, var(--grain-dark) 55%, rgba(217,154,43,0) 72%);
    opacity: 0.85;
  }
  .grain-photo--top-left { left: -40px; top: -20px; width: 210px; height: 110px; }
  .grain-photo--left { left: -50px; top: 180px; width: 260px; height: 170px; }
  .grain-photo--top-right { right: -60px; top: 20px; width: 200px; height: 170px; }
  .grain-photo--bottom-right { right: -50px; top: 260px; width: 180px; height: 100px; }

  .brand {
    position: absolute;
    left: 55px;
    top: 87px;
    display: flex;
    align-items: center;
    gap: 18px;
  }
  .brand-dot {
    width: 96px;
    height: 96px;
    border-radius: 50%;
    background: var(--teal);
  }
  .brand-name {
    color: var(--teal);
    font-weight: 700;
    font-size: 50px;
    line-height: 48px;
    letter-spacing: 0.5px;
    text-transform: uppercase;
  }
  .person {
    position: absolute;
    left: 610px;
    top: 78px;
    color: var(--teal);
  }
  .person-name {
    font-size: 56px;
    line-height: 1;
    margin: 0;
    font-weight: 400;
    letter-spacing: 1px;
  }
  .person-role {
    font-size: 38px;
    margin: 10px 0 0 2px;
    line-height: 1;
  }
  .person-company {
    font-size: 32px;
    margin: 18px 0 0 -2px;
    line-height: 1;
  }
  .contact {
    position: absolute;
    left: 75px;
    top: 425px;
    color: var(--paper);
    font-size: 28px;
    line-height: 57px;
    margin: 0;
    font-style: normal;
  }
</style>
</head>
<body>
  <div class="card">
    <svg class="card-bands" width="1085" height="635" viewBox="0 0 1085 635" aria-hidden="true">
      <defs>
        <linearGradient id="goldLower" x1="0" y1="0" x2="0" y2="1">
          <stop offset="0" stop-color="#b99400"/>
          <stop offset="0.25" stop-color="var(--gold)"/>
          <stop offset="1" stop-color="var(--gold-deep)"/>
        </linearGradient>
      </defs>
      <rect x="0" y="0" width="1085" height="48" fill="var(--gold)"/>
      <rect x="0" y="48" width="1085" height="272" fill="var(--paper)"/>
      <rect x="0" y="320" width="1085" height="60" fill="url(#goldLower)"/>
      <polygon points="0,378 1085,338 1085,418 0,395" fill="var(--teal-band)"/>
      <polyline points="0,378 1085,338" stroke="#ffffff" stroke-width="2" fill="none"/>
      <polygon points="0,395 1085,418 1085,635 0,635" fill="var(--ink)"/>
      <polyline points="0,395 1085,418" stroke="#ffffff" stroke-width="2" fill="none"/>
    </svg>

    <div class="grain-photo grain-photo--top-left" role="img" aria-label="Photo of scattered golden rice grains"></div>
    <div class="grain-photo grain-photo--left" role="img" aria-label="Photo of scattered golden rice grains"></div>
    <div class="grain-photo grain-photo--top-right" role="img" aria-label="Photo of scattered golden rice grains"></div>
    <div class="grain-photo grain-photo--bottom-right" role="img" aria-label="Photo of scattered golden rice grains"></div>

    <div class="brand">
      <div class="brand-dot"></div>
      <div class="brand-name">Larkfield<br>Milling</div>
    </div>

    <div class="person">
      <h1 class="person-name">DALE VOSKO</h1>
      <p class="person-role">Construction Manager</p>
      <p class="person-company">LARKFIELD MILLING CO.</p>
    </div>

    <address class="contact">
      LLC 3870 WILBUR HASTINGS DRIVE PINE BLUFF, AR 71601<br>
      CELL: 501-555-0142<br>
      dalevosko@larkfieldmills.example
    </address>
  </div>
</body>
</html>
```